Business cards Dör Kornhüüs GmbH & Co.KG

We need a uniform business card design template for our employees.
A template should be created to have the same design for all business cards.

Contact Information for Business Card

Firma und Firmierung, Name, Funktion in Unternehmen, Anschrift, Tel. Handynummer, Emailadresse, Internetseite

Colors

Designer to choose colors to be used in the design.

Requirements
Must have
• Our company logo must be on it

```html
<!DOCTYPE html>
<html lang="de">
<head>
<meta charset="utf-8">
<title>Dör Kornhüüs – Visitenkarte</title>
<link rel="stylesheet" href="https://fonts.googleapis.com/css2?family=Arimo:wght@400;700&display=swap">
<style>
  :root {
    --stage: #d3d3d3;
    --paper: #ffffff;
    --ink-dark: #1a1a1a;
    --rose: #f0707c;
    --lilac: #c59ccb;
    --text-grey: #6e6e6e;
  }
  * { box-sizing: border-box; margin: 0; padding: 0; }
  html, body { width: 1000px; height: 1200px; overflow: hidden; }
  body {
    background: var(--stage);
    font-family: "Arimo", Arial, sans-serif;
    position: relative;
  }
  .card {
    position: absolute;
    box-shadow: 0 10px 28px rgba(0,0,0,0.45);
  }
  .card--front { left: 111px; top: 120px; width: 777px; height: 446px; background: var(--paper); }
  .card--back { left: 109px; top: 633px; width: 782px; height: 446px; background: var(--ink-dark); }

  .brand { position: absolute; display: flex; align-items: center; color: var(--rose); font-weight: 400; white-space: nowrap; }
  .brand__dot { border-radius: 50%; background: var(--lilac); flex: none; }
  .card--front .brand { left: 57px; top: 88px; font-size: 44px; gap: 14px; }
  .card--front .brand__dot { width: 26px; height: 26px; }
  .card--back .brand { left: 50%; top: 50%; transform: translate(-50%, -50%); font-size: 58px; gap: 18px; }
  .card--back .brand__dot { width: 34px; height: 34px; }

  .holder { position: absolute; right: 53px; top: 220px; text-align: right; }
  .holder__name { color: var(--rose); font-size: 25px; font-weight: 700; line-height: 32px; }
  .holder__role { color: var(--text-grey); font-size: 16px; line-height: 22px; }

  .divider { position: absolute; left: 57px; right: 53px; top: 291px; height: 2px; background: var(--lilac); }

  .contact { position: absolute; left: 57px; top: 311px; list-style: none; }
  .contact li { display: flex; align-items: center; height: 25px; color: var(--text-grey); font-size: 17px; }
  .contact svg { width: 16px; height: 16px; margin-right: 11px; fill: var(--rose); flex: none; }

  .address { position: absolute; right: 53px; top: 336px; text-align: right; font-style: normal; color: var(--text-grey); font-size: 17px; line-height: 25px; }

  .band { position: absolute; left: 0; bottom: 0; width: 777px; height: 18px; }
</style>
</head>
<body>
  <section class="card card--front">
    <div class="brand"><span class="brand__dot"></span>Dör Kornhüüs</div>

    <div class="holder">
      <p class="holder__name">Jonas Petersen</p>
      <p class="holder__role">Owner</p>
    </div>

    <div class="divider"></div>

    <ul class="contact">
      <li><svg viewBox="0 0 16 16"><path d="M3.5 1l2.5 3-1.5 1.8c.8 1.9 2.3 3.4 4.2 4.2L10.5 8.5l3 2.5-1.2 2.6c-.3.6-1 .9-1.6.7C5.900 12.900 3.100 10.100 1.700 5.300c-.2-.6.1-1.300.7-1.600z"/></svg>000.123.456.789</li>
      <li><svg viewBox="0 0 16 16"><path d="M4.5 0h7a1.5 1.5 0 0 1 1.5 1.5v13A1.5 1.5 0 0 1 11.5 16h-7A1.5 1.5 0 0 1 3 14.5v-13A1.5 1.5 0 0 1 4.5 0zm0 1.3v11.2h7V1.3zM8 13.3a.8.8 0 1 0 0 1.6.8.8 0 0 0 0-1.6z"/></svg>000.123.456.789</li>
      <li><svg viewBox="0 0 16 16"><path d="M1 3h14v1.2L8 8.6 1 4.2zm0 2.6l7 4.400 7-4.400V13H1z"/></svg>info@yourwebsitename.com</li>
      <li><svg viewBox="0 0 16 16"><path d="M8 1a7 7 0 1 0 0 14A7 7 0 0 0 8 1zm5.600 6.300h-2.500a11 11 0 0 0-.9-4.100 5.700 5.700 0 0 1 3.400 4.100zM8 2.400c.7.9 1.600 2.600 1.800 4.900H6.200C6.400 5 7.300 3.300 8 2.400zM5.800 3.200a11 11 0 0 0-.9 4.100H2.400a5.700 5.700 0 0 1 3.400-4.100zM2.400 8.700h2.500a11 11 0 0 0 .9 4.100 5.700 5.700 0 0 1-3.400-4.100zM8 13.600c-.7-.9-1.600-2.600-1.800-4.900h3.600c-.2 2.300-1.100 4-1.800 4.900zm2.200-.8a11 11 0 0 0 .9-4.100h2.500a5.700 5.700 0 0 1-3.400 4.100z"/></svg>www.yourwebsitename.com</li>
    </ul>

    <address class="address">
      2810 Harbor Lane<br>
      Suite 45<br>
      Elmbrook, MD 20417
    </address>

    <svg class="band" viewBox="0 0 777 18" preserveAspectRatio="none" aria-hidden="true">
      <polygon points="0,0 387,0 371,18 0,18" fill="var(--lilac)"/>
      <polygon points="399,0 777,0 777,18 383,18" fill="var(--rose)"/>
    </svg>
  </section>

  <section class="card card--back">
    <div class="brand"><span class="brand__dot"></span>Dör Kornhüüs</div>
  </section>
</body>
</html>
```